Plastering (solid plastering) business card design

We need a business card for a a small plastering business based in Perth Western Australia. We are a small team that provides a service in solid plastering specialising in float, white set and sand finish. We would like to see a clean business card with our name "Brightline Plastering" being the focus of the card and maybe incorporated into a logo. We don't have a logo at the moment so we would like to see some cards that may provide us with our future logo.

Industry/Entity Type

Business

Contact Information for Business Card

Brightline Plastering

Solid Plastering Specialists

Ph: Corey 0417683091
Ph: Liam 0468120357

Requirements
Should not have
• The design should not have Drywall incorporated into the card. In perth W.A. Plastering in different to someone that puts up Plyvane. We use sand, cement, lime and hardwall plaster.

```html
<!DOCTYPE html>
<html lang="en">
<head>
<meta charset="utf-8">
<title>Brightline Plastering – Business Card</title>
<link rel="stylesheet" href="https://fonts.googleapis.com/css2?family=Sorts+Mill+Goudy&family=Righteous&display=swap">
<style>
  :root {
    --frame-red: #ff0000;
    --card-white: #ffffff;
    --brand-blue: #0f0fee;
    --tagline-green: #2ccf0c;
    --band-blue: #2a82ff;
    --contact-white: #ffffff;
    --location-black: #111111;
  }
  html, body {
    margin: 0;
    padding: 0;
    overflow: hidden;
    background: #ffffff;
  }
  .card {
    position: relative;
    width: 1200px;
    height: 686px;
    background: var(--frame-red);
    overflow: hidden;
  }
  .card__face {
    position: absolute;
    left: 36px;
    top: 25px;
    width: 1129px;
    height: 640px;
    background: var(--card-white);
  }
  .brand {
    position: absolute;
    left: 0;
    right: 0;
    text-align: center;
    font-family: "Sorts Mill Goudy", "Goudy Old Style", serif;
    margin: 0;
    font-weight: 400;
    line-height: 1;
  }
  .brand__name {
    top: 114px;
    font-size: 68px;
    color: var(--brand-blue);
  }
  .brand__tagline {
    top: 188px;
    font-size: 34px;
    color: var(--tagline-green);
  }
  .contact-band {
    position: absolute;
    left: 0;
    top: 309px;
    width: 100%;
    height: 201px;
    background: var(--band-blue);
  }
  .contact {
    position: absolute;
    top: 0;
    width: 400px;
    text-align: center;
    font-family: "Righteous", "Arial Black", sans-serif;
    color: var(--contact-white);
    line-height: 1;
  }
  .contact--corey { left: 34px; }
  .contact--liam { left: 655px; }
  .contact__name {
    position: absolute;
    left: 0;
    right: 0;
    top: 47px;
    font-size: 50px;
    letter-spacing: 2px;
  }
  .contact__phone {
    position: absolute;
    left: 0;
    right: 0;
    top: 108px;
    font-size: 50px;
    letter-spacing: 4px;
  }
  .contact--liam .contact__phone { top: 114px; left: 16px; }
  .location {
    position: absolute;
    left: 0;
    right: 0;
    top: 550px;
    margin: 0;
    text-align: center;
    font-family: "Sorts Mill Goudy", "Goudy Old Style", serif;
    font-size: 38px;
    color: var(--location-black);
    line-height: 1;
  }
</style>
</head>
<body>
  <div class="card">
    <div class="card__face">
      <h1 class="brand brand__name">Brightline Plastering</h1>
      <p class="brand brand__tagline">Solid Plastering Specialists</p>

      <div class="contact-band">
        <div class="contact contact--corey">
          <div class="contact__name">Corey</div>
          <div class="contact__phone">0417683091</div>
        </div>
        <div class="contact contact--liam">
          <div class="contact__name">Liam</div>
          <div class="contact__phone">0468120357</div>
        </div>
      </div>

      <p class="location">Perth,Western Australia</p>
    </div>
  </div>
</body>
</html>
```